Morrow Maddox LLP Logo & Stationery

We need to design a logo and stationary for a new high-end boutique matrimonial law firm in NY. We would like to see designed that use a M2 (M squared) logo. We will have offices in 3 locations so we would like to compare layouts that have the 3 locations or 1 location on the letterhead. We are open to color selection, but would like to see designed that use the colors light grey, bright light blue/teal, orange or black. The final design should communicate professional and upscale, yet be fresh and have a modern feel.

Industry/Entity Type

Legal

Font styles to use
Sans Serif

Colors
d5d5d5
0493ce
f68e4e
474747

Requirements
Must have
• I would like see a design of the letterhead to have the following addresses:
• Manhattan Office
• 612 Linden Avenue, 31st Floor
• New York, New York 10093
• Queens Office
• 204-61 Garrison Boulevard, 14th Floor
• Forest Hills, New York 11392
Nice to have
• I would like to see a design logo option that has an M squared symbol in a box almost like it looks like from the Element Table.
Should not have
• Should not feel like a logo for an ad agency or something campy.

```html
<!DOCTYPE html>
<html lang="en">
<head>
<meta charset="utf-8">
<title>Morrow Maddox LLP — Logo &amp; Letterhead</title>
<link rel="stylesheet" href="https://fonts.googleapis.com/css2?family=Cinzel:wght@600;700&family=Montserrat:wght@400;600&display=swap">
<style>
  :root {
    --brand-blue: #0493ce;
    --brand-charcoal: #474747;
    --brand-grey: #d5d5d5;
    --faint-grey: #e6e6e6;
    --backdrop: #f4f4f4;
    --paper: #ffffff;
    --ink: #222222;
  }
  * { margin: 0; padding: 0; box-sizing: border-box; }
  html, body { width: 1200px; height: 900px; overflow: hidden; }
  body {
    background: var(--backdrop);
    position: relative;
    font-family: "Montserrat", sans-serif;
    color: var(--ink);
  }

  /* Primary logo lockup: plain square beside the firm name */
  .brand-square {
    position: absolute;
    left: 230px; top: 346px;
    width: 153px; height: 152px;
    background: var(--brand-blue);
    border: 5px solid var(--brand-charcoal);
  }
  .brand-name {
    position: absolute;
    left: 52px; width: 512px; top: 508px;
    text-align: center;
    font-family: "Cinzel", serif;
    font-weight: 700;
    font-size: 45px;
    line-height: 56px;
    letter-spacing: 0;
    color: var(--brand-charcoal);
    white-space: nowrap;
  }

  /* Letterhead sheet */
  .letterhead {
    position: absolute;
    left: 613px; top: 107px;
    width: 532px; height: 685px;
    background: var(--paper);
  }
  .letterhead-square {
    position: absolute;
    left: 165px; top: 39px;
    width: 47px; height: 47px;
    background: var(--brand-blue);
    border: 2px solid var(--brand-charcoal);
  }
  .letterhead-name {
    position: absolute;
    left: 104px; width: 170px; top: 90px;
    text-align: center;
    font-family: "Cinzel", serif;
    font-weight: 700;
    font-size: 13.5px;
    line-height: 18px;
    color: var(--brand-charcoal);
    white-space: nowrap;
  }
  .office {
    position: absolute;
    left: 343px;
    font-style: normal;
    font-size: 8.6px;
    line-height: 10.2px;
    color: var(--ink);
  }
  .office--manhattan { top: 38px; }
  .office--queens { top: 88px; left: 342px; }

  .letter-body {
    position: absolute;
    left: 116px; top: 175px;
    width: 373px;
    font-size: 7.2px;
    line-height: 15.2px;
  }
  .letter-body p { text-align: justify; margin-bottom: 15.2px; }
  .letter-body .greeting, .letter-body .closing { text-align: left; }
  .letter-body .signature { font-weight: 600; font-size: 6.8px; margin-top: 12px; }

  .footer-rule {
    position: absolute;
    left: 40px; top: 635px;
    width: 313px; height: 7px;
    background: var(--brand-blue);
  }
  .footer-square {
    position: absolute;
    left: 377px; top: 543px;
    width: 102px; height: 102px;
    background: var(--faint-grey);
  }
</style>
</head>
<body>
  <div class="brand-square"></div>
  <div class="brand-name">Morrow Maddox LLP</div>

  <section class="letterhead">
    <div class="letterhead-square"></div>
    <div class="letterhead-name">Morrow Maddox LLP</div>

    <address class="office office--manhattan">
      Manhattan Office<br>
      612 Linden Avenue, 31st Floor<br>
      New York, New York 10093
    </address>
    <address class="office office--queens">
      Queens Office<br>
      204-61 Garrison Boulevard, 14th Floor<br>
      Forest Hills, New York 11392
    </address>

    <div class="letter-body">
      <p class="greeting">Dear Friend,</p>
      <p>Lorem ipsum dolor sit amet, consectetur adipisicing elit, sed do eiusmod tempor incididunt ut labore et dolore magna aliqua. Ut enim ad minim veniam, quis nostrud exercitation ullamco laboris nisi ut aliquip ex ea commodo consequat. Duis aute irure dolor in reprehenderit in voluptate velit esse cillum dolore eu fugiat nulla pariatur. Excepteur sint occaecat cupidatat non proident, sunt in culpa qui officia deserunt mollit anim id est laborum.</p>
      <p>Duis aute irure dolor in reprehenderit in voluptate velit esse cillum dolore eu fugiat nulla pariatur. Excepteur sint occaecat cupidatat non proident. Lorem ipsum dolor sit amet, consectetur adipisicing elit, sed do eiusmod tempor incididunt ut labore et dolore magna aliqua. Ut enim ad minim veniam, quis nostrud exercitation ullamco laboris nisi ut aliquip ex ea commodo consequat. Duis aute irure dolor in reprehenderit in voluptate velit esse cillum dolore eu fugiat nulla pariatur. Excepteur sint occaecat cupidatat non proident, sed do eiusmod tempor incididunt ut labore et dolore magna aliqua. Ut enim ad minim veniam, quis nostrud exercitation ullamco laboris nisi ut aliquip ex ea commodo consequat.</p>
      <p>Excepteur sint occaecat cupidatat non proident, sunt in culpa qui officia deserunt mollit anim id est laborum. Lorem ipsum dolor sit amet, consectetur adipisicing elit, sed do eiusmod tempor incididunt ut labore et dolore magna aliqua.</p>
      <p class="closing">Best Regards.</p>
      <p class="signature">Daniel R. Whitcomb</p>
    </div>

    <div class="footer-rule"></div>
    <div class="footer-square"></div>
  </section>
</body>
</html>
```